Business Cards for Internet Security Company

Awesome designers! This is the opportunity to help design cards for a forward thinking network security company. They use threat information gathered from peer groups to make intelligent decisions on what threats are relevant and which arent. ( not that you need this to do designs, but just so you know where they are coming from. ) :-)

We'd like to see a two side design and the deliverables will be in illustrator 4. The logo is attached and the logo colors are attached in the JPG and I've attached a an eps of the logo and icon

```html
<!DOCTYPE html>
<html lang="en">
<head>
<meta charset="utf-8">
<title>Kestrelgate Business Cards</title>
<link href="https://fonts.googleapis.com/css2?family=Questrial&display=swap" rel="stylesheet">
<style>
  :root {
    --page: #dcdcdc;
    --navy-teal: #245f7e;
    --pale-steel: #b4c8d4;
    --paper: #ffffff;
    --rule: #245f7e;
    --ink: #2b2b2b;
    --ink-soft: #6b6b6b;
    --mark-blue: #2f86c3;
    --edge: #000000;
  }
  html, body {
    margin: 0;
    width: 1200px;
    height: 750px;
    overflow: hidden;
    background: var(--page);
    font-family: "Questrial", "Century Gothic", sans-serif;
  }
  .canvas {
    position: relative;
    width: 1200px;
    height: 750px;
  }
  .card {
    position: absolute;
    top: 238px;
    width: 480px;
    height: 274px;
    border-radius: 22px;
    overflow: hidden;
    background: var(--paper);
    box-shadow: 0 3px 10px rgba(0,0,0,0.18);
  }
  .card--back { left: 90px; }
  .card--front { left: 630px; }

  /* back side stripes */
  .band { position: absolute; left: 0; width: 100%; }
  .band--dark { background: var(--navy-teal); }
  .band--pale { background: var(--pale-steel); }
  .hairline { position: absolute; left: 0; width: 100%; height: 1.5px; background: var(--rule); }

  .brand {
    position: absolute;
    display: flex;
    align-items: center;
    gap: 8px;
    color: var(--navy-teal);
    font-size: 30px;
    line-height: 1;
    letter-spacing: 0.5px;
  }
  .brand__dot {
    width: 22px;
    height: 22px;
    border-radius: 50%;
    background: var(--mark-blue);
    flex: none;
  }
  .card--back .brand { left: 0; right: 0; top: 123px; justify-content: center; }

  /* front side */
  .front-art { position: absolute; inset: 0; }
  .card--front .brand { left: 28px; top: 106px; }
  .holder {
    position: absolute;
    left: 62px;
    top: 150px;
  }
  .holder__name {
    margin: 0;
    font-size: 20px;
    color: var(--ink);
    letter-spacing: 0.3px;
  }
  .holder__role {
    margin: 2px 0 0;
    font-size: 10px;
    color: var(--ink-soft);
  }
  .contact {
    position: absolute;
    left: 34px;
    bottom: 22px;
    margin: 0;
    padding: 0;
    list-style: none;
    color: var(--paper);
    font-size: 11px;
    line-height: 15px;
    letter-spacing: 0.3px;
  }
</style>
</head>
<body>
<main class="canvas">

  <section class="card card--back" aria-label="Card back">
    <div class="band band--dark" style="top:0;height:68px"></div>
    <div class="hairline" style="top:80px"></div>
    <div class="band band--pale" style="top:92px;height:26px"></div>
    <div class="brand"><span class="brand__dot"></span>Kestrelgate</div>
    <div class="band band--pale" style="top:162px;height:26px"></div>
    <div class="hairline" style="top:196px"></div>
    <div class="band band--dark" style="top:208px;height:66px"></div>
  </section>

  <section class="card card--front" aria-label="Card front">
    <svg class="front-art" width="480" height="274" viewBox="0 0 480 274" aria-hidden="true">
      <rect width="480" height="274" fill="var(--paper)"/>
      <rect x="0" y="16" width="480" height="1.5" fill="var(--rule)"/>
      <rect x="0" y="40" width="480" height="30" fill="var(--pale-steel)"/>
      <rect x="0" y="136" width="480" height="1.5" fill="var(--rule)"/>
      <rect x="0" y="186" width="480" height="24" fill="var(--pale-steel)"/>
      <polygon points="0,222 480,88 480,274 0,274" fill="var(--navy-teal)"/>
      <polygon points="120,188 480,86 480,91 120,193" fill="var(--edge)"/>
    </svg>
    <div class="brand"><span class="brand__dot"></span>Kestrelgate</div>
    <div class="holder">
      <p class="holder__name">John Doe</p>
      <p class="holder__role">Director</p>
    </div>
    <ul class="contact">
      <li>0000-1234-5678</li>
      <li>www.quillfield.net</li>
      <li>jdoe@quillfield.net</li>
    </ul>
  </section>

</main>
</body>
</html>
```